Valentines Day Helicopter Tour Mailer

The purpose behind this project is to design a mailer for helicopter tours around valentines day. Not sure exaclty all what to include as i'm not sure if i want to price on it yet but i want helicopters, hearts, and something interesting to draw attention to the service we will be offering. If we did include price it would be $169/ person. Size should be good for 8.5 by 11 paper

Target Market(s)

general public

```html
<!DOCTYPE html>
<html lang="en">
<head>
<meta charset="utf-8">
<title>Valentines Day Helicopter Tour Mailer</title>
<link rel="stylesheet" href="https://fonts.googleapis.com/css2?family=Poppins:ital,wght@0,400;0,600;0,700;1,600&family=Courgette&display=swap">
<style>
  :root {
    --stage: #5a5a5a;
    --red-deep: #6e0d10;
    --red: #c8161d;
    --red-bright: #e3232a;
    --gold: #f6c343;
    --white: #ffffff;
    --paper: #ececec;
    --ink: #1c1c1c;
    --silver-dark: #6d6d6d;
    --silver-light: #f2f2f2;
  }
  * { margin: 0; padding: 0; box-sizing: border-box; }
  html, body { width: 1200px; height: 2192px; overflow: hidden; }
  body { background: var(--stage); font-family: "Poppins", sans-serif; position: relative; }

  .mailer {
    position: absolute; left: 60px; top: 378px;
    width: 1080px; height: 1435px; overflow: hidden;
    background: var(--red-deep);
    box-shadow: 0 20px 50px rgba(0,0,0,.45);
  }
  .photo-backdrop {
    position: absolute; inset: 0;
    background:
      radial-gradient(ellipse 55% 35% at 82% 28%, rgba(20,4,4,.85), transparent 70%),
      linear-gradient(180deg, #8f1418 0%, #b8171d 35%, #b33a20 62%, #6f7a3a 82%, #3c3c3c 100%);
  }
  .photo-helicopter {
    position: absolute; left: 610px; top: 210px; width: 470px; height: 330px;
    background: radial-gradient(ellipse at 60% 55%, rgba(15,8,8,.9), rgba(60,10,10,.2) 70%, transparent);
  }

  .brand {
    position: absolute; left: 73px; top: 90px;
    display: flex; align-items: center; gap: 16px;
    color: var(--white); font-weight: 700; font-size: 44px; letter-spacing: .5px;
  }
  .brand-dot { width: 38px; height: 38px; border-radius: 50%; background: var(--white); }

  .headline { position: absolute; left: 78px; top: 240px; color: var(--white); }
  .headline-main { font-weight: 700; font-size: 94px; line-height: 92px; letter-spacing: 2px; }
  .headline-sub { font-size: 44px; line-height: 60px; margin-top: 6px; }
  .headline-script {
    font-family: "Courgette", cursive; color: var(--gold);
    font-size: 80px; line-height: 90px; text-shadow: 0 3px 8px rgba(0,0,0,.35);
  }

  .heart-photo { position: absolute; left: 52px; top: 628px; width: 530px; height: 430px; }
  .price {
    position: absolute; left: 150px; top: 760px; width: 300px;
    text-align: center; color: var(--white);
  }
  .price-amount { color: var(--gold); font-weight: 700; font-size: 88px; line-height: 90px; }
  .price-unit { font-size: 31px; line-height: 36px; }

  .tour-note {
    position: absolute; left: 665px; top: 644px;
    border-left: 3px solid var(--white); padding-left: 22px;
    color: var(--white); font-size: 38px; line-height: 46px;
  }
  .tour-note strong { color: var(--gold); font-weight: 600; }

  .swoosh { position: absolute; inset: 0; width: 1080px; height: 1435px; }

  .message {
    position: absolute; left: 273px; top: 1115px; width: 650px;
    color: var(--ink); font-size: 20.5px; line-height: 31px;
  }
  .message em { color: var(--red-bright); font-weight: 600; font-size: 26px; }
  .contact-rule { position: absolute; left: 273px; top: 1267px; width: 640px; height: 2px; background: var(--ink); }
  .contact-web { position: absolute; left: 273px; top: 1300px; font-size: 21px; color: var(--ink); }
  .contact-phone {
    position: absolute; left: 660px; top: 1286px;
    display: flex; align-items: center; gap: 14px;
    font-weight: 600; font-size: 35px; color: var(--ink);
  }
</style>
</head>
<body>
  <main class="mailer">
    <div class="photo-backdrop" role="img" aria-label="Night city skyline and aerial landscape in red tones with a helicopter cockpit view"></div>
    <div class="photo-helicopter" role="img" aria-label="Helicopter parked on a helipad at night"></div>

    <div class="brand"><span class="brand-dot"></span>Aerolume Helicopters</div>

    <h1 class="headline">
      <div class="headline-main">TAKE<br>ROMANCE</div>
      <div class="headline-sub">to New Heights on this</div>
      <div class="headline-script">Valentines Day!</div>
    </h1>

    <svg class="heart-photo" viewBox="0 0 100 100" preserveAspectRatio="none" role="img" aria-label="Heart-shaped aerial photo of a pink sunset over a lake and forest">
      <defs>
        <linearGradient id="heartScene" x1="0" y1="0" x2="1" y2="1">
          <stop offset="0" stop-color="#7a2418"/>
          <stop offset=".45" stop-color="#e9a0a8"/>
          <stop offset="1" stop-color="#c96a6e"/>
        </linearGradient>
      </defs>
      <path d="M50 96 C20 72 0 52 0 30 C0 11 14 1 29 1 C40 1 47 8 50 17 C53 8 60 1 71 1 C86 1 100 11 100 30 C100 52 80 72 50 96Z" fill="url(#heartScene)"/>
      <path d="M42 88 C22 72 9 58 9 42 C9 29 18 22 28 22 C36 22 41 27 43 32 C46 27 52 22 60 22 C71 22 78 30 78 42 C78 58 63 72 42 88Z" fill="#b3151b" opacity=".92"/>
    </svg>

    <div class="price">
      <div class="price-amount">$169</div>
      <div class="price-unit">Per Person</div>
    </div>

    <p class="tour-note"><strong>HELICOPTER<br>TOURS</strong> Around<br>Great Lakes area<br>and beyond.</p>

    <svg class="swoosh" viewBox="0 0 1080 1435" aria-hidden="true">
      <defs>
        <linearGradient id="silverBand" x1="0" y1="0" x2="1" y2="0">
          <stop offset="0" stop-color="#5a5a5a"/>
          <stop offset=".35" stop-color="#f4f4f4"/>
          <stop offset=".6" stop-color="#9a9a9a"/>
          <stop offset=".85" stop-color="#ffffff"/>
          <stop offset="1" stop-color="#6d6d6d"/>
        </linearGradient>
        <linearGradient id="redBand" x1="0" y1="0" x2="1" y2="0">
          <stop offset="0" stop-color="#8a0d12"/>
          <stop offset="1" stop-color="#e3232a"/>
        </linearGradient>
      </defs>
      <path d="M0 1160 C150 980 450 900 1080 905 L1080 960 C560 955 250 1000 60 1435 L0 1435Z" fill="url(#redBand)"/>
      <path d="M40 1435 C170 1110 420 960 1080 950 L1080 1010 C560 1012 260 1080 110 1435Z" fill="url(#silverBand)"/>
      <path d="M110 1435 C150 1300 190 1180 280 1110 C380 1045 560 1020 1080 1008 L1080 1435Z" fill="var(--paper)"/>
      <path d="M540 1080 C760 1040 950 1050 1080 1100 L1080 1080 C950 1030 760 1025 540 1080Z" fill="var(--red-bright)" opacity=".9"/>
    </svg>

    <p class="message">You will feel safe at home in our helicopters because our pilots have been trained to the highest standard and we strive to be the best. <em>Come enjoy the safety, security and down right experience of a helicopter today!</em></p>
    <div class="contact-rule"></div>
    <div class="contact-web">www.aerolumeheli.com</div>
    <div class="contact-phone">
      <svg width="26" height="26" viewBox="0 0 24 24" aria-hidden="true"><path fill="var(--red-bright)" d="M6.6 10.8a15.1 15.1 0 0 0 6.6 6.6l2.2-2.2a1 1 0 0 1 1-.25 11.4 11.4 0 0 0 3.6.57 1 1 0 0 1 1 1V20a1 1 0 0 1-1 1A17 17 0 0 1 3 4a1 1 0 0 1 1-1h3.5a1 1 0 0 1 1 1c0 1.25.2 2.45.57 3.57a1 1 0 0 1-.25 1z"/></svg>
      555-014-0188
    </div>
  </main>
</body>
</html>
```